Coffee House With Cycling Theme Wants Business Cards

We want to create a business card for a coffee house that has a cycling theme. We expect to use the current logo on one side of the business card and we have been considering adding the words 'COFFEE HOUSE' underneath (see example). For the other side of the business card we want an interesting design with tag-line, address and social media links (the normal business card stuff). See examples provided but we are not fixed on having it exactly as shown, we are very open to great creative ideas. Please note our logo has the initials ‘RM' in orange embedded in the design and this must be retained. However, you can play with the words COFFEE HOUSE as well as use the orange color on the backside of the business card, as you see fit. For an image on the backside of the business card it can be a photo, hand-drawn or whatever but it must visually combine coffee and cycling in some way. The interior of the Coffee House will be reclaimed wood, rustic and have an urban feel to it with cycling artifacts hanging from the walls/ceiling, etc. Finally, it would be beneficial if the business card design elements can be easily used on flyers and other promotional assets. Good luck, we are looking forward to seeing your creative ideas.

Target Market(s)

Coffee lovers and cycling fans

Contact Information for Business Card

See project description.

Colors

Designer to choose colors to be used in the design.

Requirements
Must have
• Must use the current logo provided and combine a coffee and bike theme.
Nice to have
• Orange is used in current logo and could be used as an accent color on the backside of the business card.

```html
<!DOCTYPE html>
<html lang="en">
<head>
<meta charset="utf-8">
<title>RM Coffee House – Business Card</title>
<link rel="stylesheet" href="https://fonts.googleapis.com/css2?family=Montserrat:wght@400;800&display=swap">
<style>
  :root {
    --backdrop: #c9c9cb;
    --card: #ffffff;
    --orange: #f26a2a;
    --ink: #1c1c1c;
    --light: #ffffff;
  }
  * { margin: 0; padding: 0; box-sizing: border-box; }
  html, body { width: 1200px; height: 799px; overflow: hidden; }
  body {
    background: var(--backdrop);
    font-family: "Montserrat", sans-serif;
    display: flex;
    flex-direction: column;
    align-items: center;
    justify-content: center;
    gap: 36px;
  }
  .card {
    width: 600px;
    height: 343px;
    background: var(--card);
    position: relative;
    overflow: hidden;
  }
  .card-front .brand-band {
    position: absolute;
    left: 0; right: 0;
    top: 62px;
    height: 170px;
    background: var(--orange);
    display: flex;
    flex-direction: column;
    align-items: center;
    justify-content: center;
  }
  .brand-name {
    color: var(--light);
    font-weight: 800;
    text-align: center;
    line-height: 1;
    letter-spacing: 0.5px;
  }
  .brand-name .initials { display: block; font-size: 40px; margin-bottom: 6px; }
  .brand-name .words { display: block; font-size: 34px; }
  .card-back svg { display: block; }
  .contact-text { font-family: "Montserrat", sans-serif; font-size: 14px; fill: var(--ink); }
  .back-brand { font-family: "Montserrat", sans-serif; font-weight: 800; fill: var(--light); }
</style>
</head>
<body>
  <section class="card card-front" aria-label="Card front">
    <div class="brand-band">
      <div class="brand-name">
        <span class="initials">RM</span>
        <span class="words">COFFEE HOUSE</span>
      </div>
    </div>
  </section>

  <section class="card card-back" aria-label="Card back">
    <svg width="600" height="343" viewBox="0 0 600 343">
      <circle cx="100" cy="200" r="250" fill="var(--orange)"/>
      <text class="back-brand" x="150" y="170" text-anchor="middle" font-size="34">RM</text>
      <text class="back-brand" x="150" y="206" text-anchor="middle" font-size="28">COFFEE HOUSE</text>

      <path d="M 292 40 A 250 250 0 0 1 335 285" fill="none" stroke="var(--ink)" stroke-width="2.5"/>
      <circle cx="292" cy="40" r="4" fill="var(--ink)"/>
      <circle cx="335" cy="285" r="4" fill="var(--ink)"/>

      <g class="contact-icons" fill="var(--card)" stroke="var(--ink)" stroke-width="2">
        <circle cx="313.5" cy="70" r="13"/>
        <circle cx="335" cy="115" r="13"/>
        <circle cx="346.8" cy="160" r="13"/>
        <circle cx="350" cy="205" r="13"/>
        <circle cx="345" cy="250" r="13"/>
      </g>
      <g class="social-marks" fill="var(--ink)">
        <circle cx="313.5" cy="70" r="6"/>
        <circle cx="335" cy="115" r="6"/>
      </g>
      <g class="mail-icon" fill="none" stroke="var(--ink)" stroke-width="1.6">
        <rect x="339.8" y="155" width="14" height="10" rx="1"/>
        <path d="M 339.8 155 L 346.8 161 L 353.8 155"/>
      </g>
      <g class="globe-icon" fill="none" stroke="var(--ink)" stroke-width="1.4">
        <circle cx="350" cy="205" r="7"/>
        <ellipse cx="350" cy="205" rx="3" ry="7"/>
        <line x1="343" y1="205" x2="357" y2="205"/>
      </g>
      <g class="pin-icon">
        <path d="M 345 259 C 340 252 339 249 339 246 A 6 6 0 0 1 351 246 C 351 249 350 252 345 259 Z" fill="var(--ink)"/>
        <circle cx="345" cy="246" r="2" fill="var(--card)"/>
      </g>

      <text class="contact-text" x="337" y="75">rmcoffeehouse</text>
      <text class="contact-text" x="358" y="120">rmcoffeehouse</text>
      <text class="contact-text" x="370" y="165">info@rmcoffeehouse.com</text>
      <text class="contact-text" x="373" y="210">www.rmcoffeehouse.com</text>
      <text class="contact-text" x="368" y="255">Maple Court, Riverton</text>
    </svg>
  </section>
</body>
</html>
```